Web Design Project

We need a web design new company based in Australia. We're a search engine marketing company who predominantly manages Vexora bidlines campaigns.
Currently still deciding on a business name so lets use “Marlow Tappers” for now.
Target market....
small to medium size businesses
- more clicks to their website from the 1st page of Vexora
- more relevant, (higher quality) clicks
- higher return on investment from their bidlines campaign
- more sales, leads, (conversions)
We'd like clean, simple, semi-professional as we'd like to pick up some high end corporate clients.
A website that we love the look and feel of – but they’re a direct competitor so can’t be too similar in design.
http://www.brindlepath.com.au/search-engine-marketing.html
**please check portfolio on this web page..they designs are absolutely stunning!! http://www.brindlepath.com.au/website-design.html
Updates
Please refer to the attached file, a rough sketch of my web page.
place replace...."Afraid your bidlines campaign is underperforming with,....
Industry/Entity Type
Business
Look and feel

```html
<!DOCTYPE html>
<html lang="en">
<head>
<meta charset="utf-8">
<title>Marlow Tappers</title>
<link rel="stylesheet" href="https://fonts.googleapis.com/css2?family=Noto+Serif&family=Open+Sans:wght@400;600&display=swap">
<style>
  :root {
    --orange: #f05a28;
    --sky-light: #eef0f2;
    --sky-mid: #c3c8cc;
    --slate: #4a4d51;
    --header: #3b3b3c;
    --header-dark: #2f2f30;
    --nav: #444546;
    --footer: #434446;
    --ink: #2f2f2f;
    --body-text: #3a3a3a;
    --line: #e2e2e2;
    --white: #ffffff;
    --button-dark: #4a4b4d;
  }
  * { margin: 0; padding: 0; box-sizing: border-box; }
  html, body { width: 1082px; height: 1200px; overflow: hidden; }
  body {
    position: relative;
    font-family: "Open Sans", Arial, sans-serif;
    background:
      linear-gradient(to bottom, transparent 485px, var(--slate) 485px),
      radial-gradient(ellipse 620px 420px at 541px 200px, var(--sky-light), var(--sky-mid) 80%, #aeb4b9);
  }
  .horizon { position: absolute; left: 0; top: 484px; width: 1082px; height: 1px; background: #8c9296; }

  .feedback-tab {
    position: absolute; left: 0; top: 183px; width: 24px; height: 91px;
    background: var(--orange); border-radius: 0 4px 4px 0;
    color: var(--white); font-size: 11px; font-weight: 600; letter-spacing: .5px;
  }
  .feedback-tab span {
    position: absolute; left: 4px; top: 60px; transform: rotate(-90deg); transform-origin: left top;
  }
  .feedback-tab svg { position: absolute; left: 6px; top: 66px; }

  .page { position: absolute; left: 170px; top: 16px; width: 745px; }

  .site-header {
    height: 90px; background: linear-gradient(var(--header), var(--header-dark));
    border-top: 3px solid var(--orange); border-radius: 3px 3px 0 0; position: relative;
  }
  .brand { position: absolute; left: 14px; top: 18px; display: flex; align-items: center; gap: 10px; }
  .brand-mark { width: 46px; height: 46px; border-radius: 50%; background: var(--orange); }
  .brand-name { font-family: "Open Sans", Arial, sans-serif; font-weight: 600; font-size: 22px; color: var(--white); line-height: 1.05; width: 110px; }
  .call-box {
    position: absolute; right: 15px; top: 6px; width: 133px; height: 24px;
    background: #2a2a2a; border-radius: 3px; font-size: 11px; line-height: 24px; text-align: center; color: #e8e8e8;
  }
  .call-box b { color: var(--orange); font-weight: 400; }
  .social { position: absolute; right: 14px; top: 52px; display: flex; gap: 4px; }
  .social i { display: block; width: 24px; height: 24px; background: #626365; border-radius: 3px; }

  .main-nav { height: 30px; background: var(--nav); display: flex; border-bottom: 1px solid #333; }
  .main-nav a {
    color: #efefef; font-size: 10.5px; text-decoration: none; line-height: 30px;
    padding: 0 15px; border-right: 1px solid #353536;
  }

  .hero {
    height: 267px;
    background: radial-gradient(ellipse 260px 200px at 300px 150px, #6d6f72, #2a2d31 60%, #111418);
  }

  .content { background: var(--white); height: 529px; position: relative; }
  .tagline {
    font-family: "Noto Serif", Georgia, serif; font-size: 18.5px; color: var(--ink);
    text-align: center; line-height: 20px; padding: 20px 60px 0; letter-spacing: .3px;
  }
  .tagline em, .callout em { font-style: normal; color: var(--orange); }
  .dotted-rule { position: absolute; left: 14px; right: 16px; top: 89px; border-top: 3px dotted #dcdcdc; }

  .services { position: absolute; left: 14px; top: 118px; display: flex; gap: 16px; }
  .service-card {
    width: 228px; height: 303px; border: 1px solid #dedede; border-radius: 3px;
    background: linear-gradient(#fff 70%, #f1f1f1); padding: 0 15px;
  }
  .service-card h2 {
    font-family: "Noto Serif", Georgia, serif; font-weight: 400; font-size: 14.5px; color: var(--ink);
    padding: 13px 0 4px; border-bottom: 1px dashed var(--orange);
  }
  .service-card h2 span { color: var(--orange); }
  .service-photo { height: 129px; margin-top: 8px; }
  .photo-card { background: linear-gradient(120deg, #2b2b2b, #6a6a6a 55%, #ddd); }
  .photo-bowls { background: linear-gradient(#ffffff, #dfeef6 45%, #9fc8e0 80%, #ffffff); }
  .photo-crowd { background: linear-gradient(#ffffff 15%, #8a8d93 50%, #4a4e56 85%, #ffffff); }
  .service-card p { font-size: 9.6px; line-height: 15px; color: var(--body-text); margin-top: 12px; height: 68px; }
  .service-card p em { font-style: normal; color: var(--orange); }
  .btn-more {
    display: inline-block; margin-top: 10px; background: var(--orange); color: var(--white);
    font-size: 9.5px; width: 69px; height: 21px; line-height: 21px; text-align: center; border-radius: 3px;
  }
  .callout-rule { position: absolute; left: 14px; right: 16px; top: 443px; border-top: 1px solid var(--line); }
  .callout { position: absolute; left: 62px; top: 473px; font-family: "Noto Serif", Georgia, serif; font-size: 15.5px; color: var(--ink); letter-spacing: .4px; }
  .btn-signup {
    position: absolute; left: 500px; top: 466px; width: 110px; height: 27px;
    background: var(--button-dark); color: var(--white); border-radius: 3px; font-size: 13px; line-height: 27px; text-align: center;
  }

  .site-footer { background: var(--footer); height: 252px; position: relative; border-radius: 0 0 3px 3px; }
  .footer-col { position: absolute; top: 23px; width: 165px; }
  .footer-col h3 { font-family: "Noto Serif", Georgia, serif; font-weight: 400; font-size: 11px; color: var(--orange); padding-bottom: 6px; border-bottom: 1px dashed #5a5b5d; width: 165px; }
  .footer-col p { font-size: 9.5px; line-height: 15px; color: #ededed; margin-top: 16px; }
  .footer-col a { color: var(--orange); text-decoration: none; }
  .footer-base { position: absolute; left: 14px; right: 16px; top: 192px; border-top: 1px dashed #58595b; }
  .copyright { position: absolute; left: 14px; top: 216px; font-size: 9px; color: #ececec; }
  .to-top { position: absolute; right: 16px; top: 216px; font-size: 9px; color: var(--orange); }
</style>
</head>
<body>
  <div class="horizon"></div>

  <div class="feedback-tab">
    <span>FEEDBACK</span>
    <svg width="12" height="10" viewBox="0 0 12 10"><rect x=".5" y=".5" width="11" height="9" fill="none" stroke="#fff"/><path d="M.5 .5 6 5.5 11.5 .5" fill="none" stroke="#fff"/></svg>
  </div>

  <div class="page">
    <header class="site-header">
      <div class="brand"><div class="brand-mark"></div><div class="brand-name">Marlow Tappers</div></div>
      <div class="call-box"><b>Call Us:</b> &nbsp;(555) 210-4480</div>
      <div class="social"><i></i><i></i><i></i></div>
    </header>

    <nav class="main-nav">
      <a href="#">Home</a><a href="#">About Us</a><a href="#">Vexora Bidlines</a><a href="#">Other Services</a><a href="#">Why Choose Us ?</a><a href="#">Contact Us</a>
    </nav>

    <div class="hero" role="img" aria-label="Businessman in a suit holding a floating search-marketing keyword panel in front of a server room"></div>

    <main class="content">
      <h1 class="tagline">We Create Great <em>Experiences</em> That Help Your Business Drive Strategic Online Outcomes</h1>
      <div class="dotted-rule"></div>

      <section class="services">
        <article class="service-card">
          <h2><span>1.</span> Local Bidlines</h2>
          <div class="service-photo photo-card" role="img" aria-label="Hand in a suit sleeve holding a card reading we can do"></div>
          <p>Lorem ipsum dolor sit amet, consetetur sadipscing elitr, sed diam nonumy eirmod tempor invidunt ut labore et <em>dolore</em> magna aliquyam erat, sed diam voluptua. At vero eos et accusam et</p>
          <span class="btn-more">Learn More</span>
        </article>
        <article class="service-card">
          <h2><span>2.</span> National Bidlines</h2>
          <div class="service-photo photo-bowls" role="img" aria-label="Goldfish leaping from one glass bowl into another"></div>
          <p>Lorem ipsum dolor sit amet, consetetur sadipscing elitr, sed diam nonumy eirmod tempor invidunt ut labore et dolore magna aliquyam erat, sed diam voluptua. At vero eos et accusam et</p>
          <span class="btn-more">Learn More</span>
        </article>
        <article class="service-card">
          <h2><span>3.</span> Ecommerce Bidlines</h2>
          <div class="service-photo photo-crowd" role="img" aria-label="Business handshake in front of a team of office workers"></div>
          <p>Lorem ipsum dolor sit amet, consetetur sadipscing elitr, sed diam nonumy eirmod tempor invidunt ut labore et dolore magna aliquyam erat, sed diam voluptua. At vero eos et accusam et</p>
          <span class="btn-more">Learn More</span>
        </article>
      </section>

      <div class="callout-rule"></div>
      <p class="callout">If You Can Dream It, <em>You Can Do It.</em></p>
      <span class="btn-signup">"Signup" Now!</span>
    </main>

    <footer class="site-footer">
      <div class="footer-col" style="left:14px">
        <h3>Marlow Tappers</h3>
        <p>Lorem ipsum dolor sit amet, consetetur sadipscing elitr, sed diam nonumy eirmod tempor invidunt ut labore et dolore magna aliquyam erat, sed diam voluptua.</p>
      </div>
      <div class="footer-col" style="left:197px"><h3>Links</h3></div>
      <div class="footer-col" style="left:379px"><h3>Latest Tweet</h3></div>
      <div class="footer-col" style="left:562px">
        <h3>Contact Us</h3>
        <p>42 Harbour Lane, Level 9 Quayside House Brisbane, Queensland 4000</p>
        <p>Phone: (555) 210-448<br>E-mail: <a href="#">info@marlowtappers.com</a><br>Website: <a href="#">www.marlowtappers.com</a></p>
      </div>
      <div class="footer-base"></div>
      <span class="copyright">© 2012 Marlow Tappers.</span>
      <span class="to-top">Top ↑</span>
    </footer>
  </div>
</body>
</html>
```